依頼概要
■ 依頼の目的/概要
「スリムテラス」というダイエット商品の口コミサイトのスマートフォン版を作成することになりましたので、イメージ画像をデザインしていただきたいと考えています(HTML・CSSのコーディングは不要)。
http://www.slim-terrace-mock.jp/

作成していただく画像は以下のものになります。

○トップページ
○商品の口コミページ

また、上記それぞれのページに使用する個々の画像

PC版の「スリムテラス」は既に存在しておりますので、参考にしてみてください。
○PC版のトップページ:http://www.slim-terrace-mock.jp
○PC版の商品の口コミページ:http://www.slim-terrace-mock.jp/2010/12/post-1767.html

■ 依頼詳細
こちらで完成イメージ画像を既に作成しております。
ファイルを添付しますので、これらのファイルを元に作成をお願いします。
ただし、我々はデザインの素人のため、あまり綺麗に出来ているとは思っていません。

```html
<!DOCTYPE html>
<html lang="ja">
<head>
<meta charset="utf-8">
<title>スリムテラス</title>
<link rel="stylesheet" href="https://fonts.googleapis.com/css2?family=M+PLUS+1p:wght@400;700;800&display=swap">
<style>
:root{
  --cream:#fbf4e4;
  --sky:#cfe9ef;
  --mint:#bfe3d8;
  --mint-dark:#8fcab9;
  --teal:#3f9c8a;
  --ink:#2b2b2b;
  --grey:#6f6f6f;
  --line:#d9d2c2;
  --orange:#f1a22a;
  --orange-dark:#d9861a;
  --pink:#e0457d;
  --red:#e2433a;
  --gold:#e0a82a;
  --beige:#e6dac2;
  --white:#ffffff;
}
*{box-sizing:border-box;margin:0;padding:0}
html,body{width:1200px;height:3748px;overflow:hidden}
body{font-family:"M PLUS 1p",sans-serif;color:var(--ink);background:var(--beige);position:relative}

.site-header{position:absolute;left:0;top:0;width:1200px;height:290px;background:linear-gradient(var(--sky),var(--cream) 70%)}
.brand{position:absolute;left:44px;top:30px;width:720px;height:230px;display:flex;flex-direction:column;justify-content:center}
.brand-tag{display:inline-block;align-self:flex-start;background:var(--orange);color:var(--white);font-size:32px;font-weight:700;padding:4px 22px;border-radius:10px;margin-bottom:18px}
.brand-name{display:flex;align-items:center;gap:18px;font-size:80px;font-weight:800;color:var(--teal);line-height:1;white-space:nowrap}
.brand-dot{flex:none;width:36px;height:36px;background:var(--teal);border-radius:50%}
.header-art{position:absolute;right:0;top:0;width:440px;height:290px;background:linear-gradient(120deg,#f6d9b8,#f2b9a4 50%,#e8c8d8)}

.search{position:absolute;left:0;top:290px;width:1200px;height:190px;background:var(--cream)}
.search-box{position:absolute;left:40px;top:34px;width:1120px;height:124px;background:var(--white);border:3px solid var(--line);border-radius:14px;display:flex;align-items:center;padding-left:34px;font-size:54px;color:#9a9a9a}
.search-btn{position:absolute;right:14px;top:10px;width:112px;height:98px;border-radius:12px;background:linear-gradient(var(--orange),var(--orange-dark))}

.topics{position:absolute;left:0;top:480px;width:1200px;height:380px;background:var(--cream);padding:36px 40px 0}
.topics-title{display:flex;align-items:center;gap:16px;font-size:58px;font-weight:800}
.topics-text{margin-top:26px;font-size:44px;line-height:64px;color:var(--grey)}
.topics-text em{font-style:normal;color:var(--red);font-weight:700}

.band{position:absolute;left:0;width:1200px;height:92px;background:var(--mint);display:flex;align-items:center;gap:18px;padding-left:36px;font-size:48px;font-weight:800;border-top:3px solid var(--mint-dark)}

.reviews{position:absolute;left:0;top:952px;width:1200px;height:850px;background:var(--white)}
.review{height:425px;padding:34px 40px 0;border-bottom:3px solid var(--line)}
.review-name{font-size:54px;font-weight:800}
.review-meta{display:flex;align-items:center;margin-top:10px;height:64px;white-space:nowrap}
.count{display:flex;align-items:center;gap:10px;color:var(--pink);font-size:44px;font-weight:700}
.stars{margin-left:auto;font-size:44px;color:var(--gold);letter-spacing:-2px}
.stars .off{color:#cfcfcf}
.user{color:var(--orange-dark);font-size:42px;font-weight:700;margin-left:14px}
.date{color:var(--grey);font-size:40px;margin-left:28px}
.review-text{margin-top:22px;font-size:42px;line-height:64px;color:var(--grey);height:128px;overflow:hidden}

.more{position:absolute;left:0;top:1802px;width:1200px;height:120px;background:var(--cream);display:flex;justify-content:flex-end;align-items:center;gap:14px;padding-right:28px;font-size:44px}

.ranking{position:absolute;left:0;top:2040px;width:1200px;height:1708px;background:var(--beige)}
.rank-label{position:absolute;left:32px;font-size:42px;font-weight:700}
.rank-card{position:absolute;left:28px;width:1144px;background:var(--white);border-radius:22px;border:3px solid #d6cbb3}
.rank-row{min-height:164px;display:flex;align-items:center;padding:24px 30px 24px 28px;border-bottom:3px dashed var(--line)}
.rank-row:last-child{border-bottom:none}
.rank-badge{flex:none;width:110px;display:flex;flex-direction:column;align-items:center;font-size:36px}
.rank-body{flex:1;margin-left:26px}
.rank-title{font-size:46px;line-height:56px;font-weight:700;color:var(--teal)}
.rank-body .count{margin-top:6px;font-size:40px}
.chev{flex:none;width:30px;height:50px}
</style>
</head>
<body>
<header class="site-header">
  <div class="brand">
    <span class="brand-tag">口コミ情報満載!の</span>
    <div class="brand-name"><span class="brand-dot"></span>スリムテラス</div>
  </div>
  <div class="header-art" role="img" aria-label="カフェでお茶を楽しむ女性たちのイラスト"></div>
</header>

<section class="search">
  <div class="search-box">ダイエット商品を検索
    <span class="search-btn">
      <svg width="112" height="98" viewBox="0 0 112 98"><circle cx="50" cy="44" r="20" fill="none" stroke="#fff" stroke-width="8"/><line x1="64" y1="58" x2="80" y2="74" stroke="#fff" stroke-width="10" stroke-linecap="round"/></svg>
    </span>
  </div>
</section>

<section class="topics">
  <h2 class="topics-title">
    <svg width="64" height="64" viewBox="0 0 64 64"><path d="M10 26h36v14a16 16 0 0 1-16 16h-4A16 16 0 0 1 10 40z" fill="#8a5a3a"/><path d="M46 30h6a7 7 0 0 1 0 14h-6" fill="none" stroke="#8a5a3a" stroke-width="5"/><path d="M22 6q6 7 0 14M32 6q6 7 0 14" stroke="#e0a82a" stroke-width="4" fill="none"/></svg>
    トピックス
  </h2>
  <p class="topics-text">今なら<em>「痩せる!ダイエット12の習慣」</em>を口コミしてくださった方全員にプレゼント!ぜひ読んでくださいね</p>
</section>

<h2 class="band" style="top:860px">
  <svg width="44" height="44" viewBox="0 0 44 44"><g fill="#3f6f63"><circle cx="22" cy="10" r="7"/><circle cx="22" cy="34" r="7"/><circle cx="10" cy="22" r="7"/><circle cx="34" cy="22" r="7"/></g><circle cx="22" cy="22" r="5" fill="#fff"/></svg>
  新着口コミ
</h2>

<section class="reviews">
  <article class="review">
    <h3 class="review-name">スリムナール</h3>
    <div class="review-meta">
      <span class="count"><svg width="48" height="40" viewBox="0 0 48 40"><path d="M4 4h40v24H20l-10 9v-9H4z" fill="#e0457d"/></svg>252</span>
      <span class="stars">★★<span class="off">★★★</span></span>
      <span class="user">ここまめ</span>
      <span class="date">2012年1月31日</span>
    </div>
    <p class="review-text">私も今日から飲み始めました 内科で一錠\210でした 162cm 61.3kg 娘の入学式までに50kg にな...</p>
  </article>
  <article class="review">
    <h3 class="review-name">エムケーティー12 -MK tea 12</h3>
    <div class="review-meta">
      <span class="count"><svg width="48" height="40" viewBox="0 0 48 40"><path d="M4 4h40v24H20l-10 9v-9H4z" fill="#e0457d"/></svg>252</span>
      <span class="stars">★★★★★</span>
      <span class="user">あずき</span>
      <span class="date">2012年1月31日</span>
    </div>
    <p class="review-text">私も今日から飲み始めました 内科で一錠\210でした 162cm 61.3kg 娘の入学式までに50kg にな...</p>
  </article>
</section>

<a class="more">
  <svg width="48" height="48" viewBox="0 0 48 48"><circle cx="24" cy="24" r="22" fill="#5a4a3a"/><path d="M19 14l11 10-11 10" stroke="#fff" stroke-width="6" fill="none"/></svg>
  もっと見る
</a>

<section class="ranking">
  <span class="rank-label" style="top:40px">ダイエット情報</span>
  <div class="rank-card" style="top:100px">
    <div class="rank-row">
      <div class="rank-badge"><svg width="96" height="60" viewBox="0 0 96 60"><path d="M8 50L4 14l24 18L48 4l20 28 24-18-4 36z" fill="#e0a82a"/></svg>1位</div>
      <div class="rank-body"><div class="rank-title">フローラルダイエット(FLORAL DIETING)</div><span class="count"><svg width="44" height="36" viewBox="0 0 48 40"><path d="M4 4h40v24H20l-10 9v-9H4z" fill="#e0457d"/></svg>32</span></div>
      <svg class="chev" viewBox="0 0 30 50"><path d="M6 6l18 19-18 19" stroke="#aaa" stroke-width="5" fill="none"/></svg>
    </div>
    <div class="rank-row">
      <div class="rank-badge"><svg width="96" height="60" viewBox="0 0 96 60"><path d="M8 50L4 14l24 18L48 4l20 28 24-18-4 36z" fill="#b9bcc2"/></svg>2位</div>
      <div class="rank-body"><div class="rank-title">正しい下半身ダイエット法</div><span class="count"><svg width="44" height="36" viewBox="0 0 48 40"><path d="M4 4h40v24H20l-10 9v-9H4z" fill="#e0457d"/></svg>32</span></div>
      <svg class="chev" viewBox="0 0 30 50"><path d="M6 6l18 19-18 19" stroke="#aaa" stroke-width="5" fill="none"/></svg>
    </div>
    <div class="rank-row">
      <div class="rank-badge"><svg width="96" height="60" viewBox="0 0 96 60"><path d="M8 50L4 14l24 18L48 4l20 28 24-18-4 36z" fill="#9a6a4a"/></svg>3位</div>
      <div class="rank-body"><div class="rank-title">シェイプムーブ+R</div><span class="count"><svg width="44" height="36" viewBox="0 0 48 40"><path d="M4 4h40v24H20l-10 9v-9H4z" fill="#e0457d"/></svg>32</span></div>
      <svg class="chev" viewBox="0 0 30 50"><path d="M6 6l18 19-18 19" stroke="#aaa" stroke-width="5" fill="none"/></svg>
    </div>
  </div>

  <span class="rank-label" style="top:700px">ダイエット情報</span>
  <div class="rank-card" style="top:760px">
    <div class="rank-row">
      <div class="rank-badge"><svg width="96" height="60" viewBox="0 0 96 60"><path d="M8 50L4 14l24 18L48 4l20 28 24-18-4 36z" fill="#e0a82a"/></svg>1位</div>
      <div class="rank-body"><div class="rank-title">フローラルダイエット(FLORAL DIETING)</div><span class="count"><svg width="44" height="36" viewBox="0 0 48 40"><path d="M4 4h40v24H20l-10 9v-9H4z" fill="#e0457d"/></svg>32</span></div>
      <svg class="chev" viewBox="0 0 30 50"><path d="M6 6l18 19-18 19" stroke="#aaa" stroke-width="5" fill="none"/></svg>
    </div>
    <div class="rank-row">
      <div class="rank-badge"><svg width="96" height="60" viewBox="0 0 96 60"><path d="M8 50L4 14l24 18L48 4l20 28 24-18-4 36z" fill="#b9bcc2"/></svg>2位</div>
      <div class="rank-body"><div class="rank-title">正しい下半身ダイエット法</div><span class="count"><svg width="44" height="36" viewBox="0 0 48 40"><path d="M4 4h40v24H20l-10 9v-9H4z" fill="#e0457d"/></svg>32</span></div>
      <svg class="chev" viewBox="0 0 30 50"><path d="M6 6l18 19-18 19" stroke="#aaa" stroke-width="5" fill="none"/></svg>
    </div>
    <div class="rank-row">
      <div class="rank-badge"><svg width="96" height="60" viewBox="0 0 96 60"><path d="M8 50L4 14l24 18L48 4l20 28 24-18-4 36z" fill="#9a6a4a"/></svg>3位</div>
      <div class="rank-body"><div class="rank-title">シェイプムーブ+R</div><span class="count"><svg width="44" height="36" viewBox="0 0 48 40"><path d="M4 4h40v24H20l-10 9v-9H4z" fill="#e0457d"/></svg>32</span></div>
      <svg class="chev" viewBox="0 0 30 50"><path d="M6 6l18 19-18 19" stroke="#aaa" stroke-width="5" fill="none"/></svg>
    </div>
  </div>
</section>

<h2 class="band" style="top:1950px">
  <svg width="44" height="44" viewBox="0 0 44 44"><g fill="#3f6f63"><circle cx="22" cy="10" r="7"/><circle cx="22" cy="34" r="7"/><circle cx="10" cy="22" r="7"/><circle cx="34" cy="22" r="7"/></g><circle cx="22" cy="22" r="5" fill="#fff"/></svg>
  口コミ評価ランキング
</h2>
</body>
</html>
```